Building showcase catalogue for a post frame construction company

We are looking for a brochure for our clients showcasing our buildings. We are a post frame building company that makes commercial, ag, homes, and other building types. We are looking for a brochure that we can use with all the types of buildings simply by changing out the pictures. We would like a more photo heavy brochure thats 1-5 pages. We want the design to feel high end luxury. Our colors are black, white, and chrome. I will upload our logo as well as some building photos in the suburban category of our buildings. We would like a page to showcase some building layouts as well.

We need the size to be us letter size.

Industry/Entity Type

Construction

Font styles to use
Serif

Colors

Designer to choose only greyscale colors for use in the design.

Requirements
Must have
• A space to showcase building photos, small text space for information. An area to showcase building layouts.
Nice to have
• I would like to have a very clean professional look thats looks high end.
Should not have
• Areas for detail pictures. We mostly have exterior building shots.

```html
<!DOCTYPE html>
<html lang="en">
<head>
<meta charset="utf-8">
<title>Harlow Builders – Building Showcase Catalogue</title>
<link rel="stylesheet" href="https://fonts.googleapis.com/css2?family=Poppins:wght@200;300;600&display=swap">
<style>
  :root {
    --canvas: #e4e4e4;
    --paper: #ffffff;
    --paper-tint: #f1f1f1;
    --charcoal: #262a2c;
    --dot: #d2d2d2;
    --ink: #1c1c1c;
    --outline: #5a5f62;
    --site-text: #2e2e2e;
  }
  * { margin: 0; padding: 0; box-sizing: border-box; }
  html, body {
    width: 1200px; height: 801px; overflow: hidden;
    background: var(--canvas);
    font-family: "Poppins", sans-serif;
  }
  .cover {
    position: absolute; left: 314px; top: 30px;
    width: 572px; height: 740px;
    background: var(--paper);
    box-shadow: 0 6px 24px rgba(0,0,0,.18);
    overflow: hidden;
  }
  .cover__band-dots {
    position: absolute; left: 0; right: 0; height: 44px;
    background-color: var(--paper-tint);
    background-image: radial-gradient(var(--dot) 1px, transparent 1.2px);
    background-size: 6px 6px;
  }
  .cover__band-dots--top { top: 0; }
  .cover__band-dots--bottom { bottom: 0; }
  .cover__spine {
    position: absolute; left: 28px; top: 44px;
    width: 196px; height: 652px;
    background: var(--charcoal);
  }
  .cover__photo {
    position: absolute; left: 206px; top: 62px;
    width: 324px; height: 596px;
    background: linear-gradient(180deg,
      #5d6b78 0%, #5d6b78 3%,
      #d8374d 4%, #e2485c 38%,
      #6f7478 48%, #8a8f7e 56%,
      #b9ac96 68%, #a89a85 100%);
  }
  .cover__word {
    position: absolute; left: 198px; top: 640px;
    transform-origin: 0 0; transform: rotate(-90deg);
    font-weight: 200; font-size: 64px; letter-spacing: 3px;
    color: transparent;
    -webkit-text-stroke: 1px var(--outline);
    white-space: nowrap;
    line-height: 1;
  }
  .cover__site {
    position: absolute; left: 520px; top: 80px;
    transform-origin: 0 0; transform: rotate(90deg);
    font-weight: 300; font-size: 17px; letter-spacing: 1px;
    color: var(--site-text);
    white-space: nowrap;
  }
  .cover__brand {
    position: absolute; left: 150px; top: 270px;
    width: 136px; height: 136px;
    background: var(--paper);
    display: flex; align-items: center; justify-content: center; gap: 6px;
    flex-direction: column;
  }
  .cover__brand-mark {
    width: 14px; height: 14px; background: var(--ink);
  }
  .cover__brand-name {
    font-weight: 600; font-size: 14px; line-height: 1.2;
    color: var(--ink); text-align: center; letter-spacing: .5px;
  }
  .cover__accent {
    position: absolute; width: 24px; height: 24px; background: var(--charcoal);
  }
  .cover__accent--one { left: 514px; top: 640px; }
  .cover__accent--two { left: 538px; top: 664px; background: #8d9194; }
</style>
</head>
<body>
  <article class="cover">
    <div class="cover__band-dots cover__band-dots--top"></div>
    <div class="cover__band-dots cover__band-dots--bottom"></div>
    <div class="cover__spine"></div>
    <div class="cover__photo" role="img" aria-label="Photo of a red metal-clad post frame building with grey wainscot, a door and barn light, above a landscaped garden with gravel and flagstone path"></div>
    <div class="cover__word">construction</div>
    <div class="cover__site">harlowbuilders.com</div>
    <div class="cover__brand">
      <span class="cover__brand-mark"></span>
      <span class="cover__brand-name">HARLOW<br>BUILDERS, INC.</span>
    </div>
    <span class="cover__accent cover__accent--one"></span>
    <span class="cover__accent cover__accent--two"></span>
  </article>
</body>
</html>
```